Update informational website

I need a new modern site design for my website.

Here is the site: http://q.zt/kmRp

Here is a theme I liked: http://q.zt/kmRb

I am looking for something with clean lines and an exciting designs and graphics, please use images from brellowtide.com and track the images used so I can buy them if I like the design.

I just need the homepage and one interior page designed.

Colors
Bright Green #6ed30d
Dark Text #222
Lighter Text #444

Number of Pages Required

2 page

Font styles to use
Sans Serif

Requirements
Must have
• Clean, good spacing, responsive design, high resolution design

```html
<!DOCTYPE html>
<html lang="en">
<head>
<meta charset="utf-8">
<title>Mesa Glass Tint</title>
<link href="https://fonts.googleapis.com/css2?family=Lato:wght@300;400;700;900&display=swap" rel="stylesheet">
<style>
:root{
  --green:#6ed30d;
  --frame:#1ed00a;
  --dark:#222;
  --text:#444;
  --muted:#888;
  --teal:#12a7c6;
  --panel:#ececec;
  --footer:#dcdcdc;
  --btn:#555;
}
*{margin:0;padding:0;box-sizing:border-box}
html,body{width:726px;height:1200px;overflow:hidden;background:#fff;font-family:'Lato',sans-serif;color:var(--text)}
.page{position:relative;width:726px;height:1200px}
.abs{position:absolute}
.topbar{left:0;top:0;width:726px;height:4px;background:#555}
.header-contact{display:flex;align-items:center;gap:8px;font-size:6.5px;letter-spacing:.6px;line-height:12px;color:var(--text)}
.header-contact b{color:var(--dark)}
.circle-icon{width:24px;height:24px;border-radius:50%;background:var(--green);display:flex;align-items:center;justify-content:center;flex:none}
.brand{left:263px;top:30px;width:200px;text-align:center;font-size:22px;font-weight:900;color:var(--green);letter-spacing:.3px}
.nav{left:0;top:91px;width:726px;display:flex;justify-content:center;gap:0;font-size:9px;font-weight:700;letter-spacing:1px;color:var(--text)}
.nav a{text-decoration:none;color:inherit;margin:0 12px}
.nav-underline{left:178px;top:120px;width:38px;height:2px;background:var(--green)}
.header-rule{left:0;top:122px;width:726px;height:1px;background:#ddd}
.hero{left:0;top:122px;width:726px;height:318px;background:linear-gradient(135deg,#3e3e3e 0%,#5a5a5a 40%,#6b6b6b 60%,#3a3a3a 100%);clip-path:polygon(0 0,100% 0,100% 276px,50% 318px,0 276px)}
.hero-title{left:0;top:208px;width:726px;text-align:center;color:var(--green);font-size:29px;font-weight:700}
.hero-sub{left:0;top:247px;width:726px;text-align:center;color:#fff;font-size:16px;font-weight:300;line-height:27px}
.btn{display:flex;align-items:center;justify-content:center;background:var(--btn);color:#fff;font-size:8.5px;font-weight:700;border-radius:5px}
.hero-btn{left:306px;top:320px;width:114px;height:24px;background:#595959}
.slider-arrow{top:231px;width:45px;height:31px;background:rgba(120,120,120,.6);display:flex;align-items:center;justify-content:center}
.section-title{text-align:center;color:var(--dark);font-weight:700}
.about-title{left:263px;top:482px;width:200px;font-size:18px}
.about-text{left:238px;top:541px;width:250px;text-align:center;font-size:8.5px;line-height:16px;color:var(--dark)}
.about-btn{left:333px;top:615px;width:61px;height:23px;font-size:8px}
.services-bg{left:0;top:664px;width:726px;height:258px;background:var(--dark);clip-path:polygon(0 40px,50% 0,100% 40px,100% 100%,0 100%)}
.services-title{left:263px;top:684px;width:200px;color:#fff;font-size:19px;text-align:center;font-weight:700}
.services-underline{left:345px;top:713px;width:36px;height:2px;background:var(--frame)}
.card-text{width:145px;text-align:center}
.card-text h3{font-size:14px;font-weight:700;color:var(--dark);letter-spacing:.4px;margin-top:12px}
.card-text p{font-size:10px;font-weight:300;color:var(--text);line-height:13px;margin-top:6px;padding:0 30px}
.card-icon{width:20px;height:20px;border-radius:3px;background:#5cb82a;margin:0 auto;display:flex;align-items:center;justify-content:center}
.contact-bg{left:0;top:922px;width:726px;height:246px;background:var(--panel)}
.contact-title{left:93px;top:950px;font-size:19px;font-weight:700;color:var(--dark)}
.contact-underline{left:93px;top:977px;width:36px;height:3px;background:var(--frame)}
.contact-lead{left:93px;top:998px;font-size:8px;color:var(--dark)}
.contact-row{left:93px;display:flex;align-items:center;gap:7px;font-size:6.5px;letter-spacing:.7px;line-height:14px;color:var(--text)}
.contact-row b{color:var(--dark)}
.contact-row .circle-icon{background:var(--teal)}
.map{left:338px;top:944px;width:286px;height:192px;background:linear-gradient(160deg,#e4e4e4,#d6d6d6)}
.footer{left:0;top:1168px;width:726px;height:32px;background:var(--footer);display:flex;align-items:center;justify-content:center;font-size:8.5px;color:#999}
</style>
</head>
<body>
<div class="page">
  <div class="abs topbar"></div>

  <div class="abs header-contact" style="left:92px;top:36px">
    <span class="circle-icon"><svg width="8" height="12" viewBox="0 0 8 12"><rect x="0.8" y="0.8" width="6.4" height="10.4" rx="1" fill="none" stroke="#fff" stroke-width="1.4"/><circle cx="4" cy="9" r=".8" fill="#fff"/></svg></span>
    <div><b>Phone:</b> 555.014.2290<br><b>Fax:</b> 555.014.2290</div>
  </div>
  <div class="abs brand">Mesa Glass Tint</div>
  <div class="abs header-contact" style="left:502px;top:36px">
    <span class="circle-icon"><svg width="10" height="13" viewBox="0 0 10 13"><path d="M5 12.5S1 7.5 1 5a4 4 0 0 1 8 0c0 2.5-4 7.5-4 7.5z" fill="#fff"/><circle cx="5" cy="5" r="1.5" fill="var(--green)"/></svg></span>
    <div><b>4120 E. Palo Verde Rd. Suite B</b><br>Tempe Ridge, Az. 85000</div>
  </div>

  <nav class="abs nav">
    <a href="#">Home</a><a href="#">Window Film Services</a><a href="#">Film</a><a href="#">About</a><a href="#">Gallery</a><a href="#">Contact</a>
  </nav>
  <div class="abs nav-underline"></div>
  <div class="abs header-rule"></div>

  <div class="abs hero" role="img" aria-label="Technician applying tint film to a car window"></div>
  <div class="abs hero-title">Mesa Glass Tint</div>
  <div class="abs hero-sub">Lorem ipsum dolor sit amet<br>consectetur adipiscing</div>
  <div class="abs btn hero-btn">Make an &nbsp;appointment</div>
  <div class="abs slider-arrow" style="left:0"><svg width="10" height="16" viewBox="0 0 10 16"><path d="M8 1 2 8l6 7" fill="none" stroke="#fff" stroke-width="1.3"/></svg></div>
  <div class="abs slider-arrow" style="left:681px"><svg width="10" height="16" viewBox="0 0 10 16"><path d="M2 1l6 7-6 7" fill="none" stroke="#fff" stroke-width="1.3"/></svg></div>
  <svg class="abs" style="left:348px;top:400px" width="30" height="20" viewBox="0 0 30 20"><path d="M3 3l12 12L27 3" fill="none" stroke="var(--frame)" stroke-width="5"/></svg>

  <svg class="abs" style="left:93px;top:462px" width="116" height="164" viewBox="0 0 116 164">
    <polygon points="0,0 115,14 115,163 0,163" fill="var(--frame)"/>
    <polygon points="6,8 109,20 109,157 6,157" fill="#7a7674" role="img" aria-label="Portrait of the shop owner beside a car"/>
  </svg>
  <svg class="abs" style="left:510px;top:462px" width="116" height="164" viewBox="0 0 116 164">
    <polygon points="0,14 115,0 115,163 0,163" fill="var(--frame)"/>
    <polygon points="6,20 109,8 109,157 6,157" fill="#2a2a2c" role="img" aria-label="Glossy black car with tinted windows"/>
  </svg>
  <div class="abs section-title about-title">About Us</div>
  <p class="abs about-text">Mesa Tinting is not just another tint shop. We specialize in one thing and one thing only; Window Tinting. We offer Residential, Commercial and Automotive tinting services.</p>
  <div class="abs btn about-btn">See More</div>

  <div class="abs services-bg"></div>
  <div class="abs services-title">Our Services</div>
  <div class="abs services-underline"></div>

  <svg class="abs" style="left:93px;top:740px" width="146" height="163" viewBox="0 0 146 163">
    <polygon points="0,17 145,0 145,162 0,162" fill="var(--frame)"/>
    <polygon points="7,23 138,8 138,155 7,155" fill="#fff"/>
  </svg>
  <svg class="abs" style="left:286px;top:740px" width="146" height="163" viewBox="0 0 146 163">
    <rect width="146" height="162" fill="var(--frame)"/>
    <rect x="7" y="7" width="132" height="148" fill="#fff"/>
  </svg>
  <svg class="abs" style="left:478px;top:740px" width="146" height="163" viewBox="0 0 146 163">
    <polygon points="0,0 145,17 145,162 0,162" fill="var(--frame)"/>
    <polygon points="7,8 138,23 138,155 7,155" fill="#fff"/>
  </svg>

  <div class="abs card-text" style="left:93px;top:780px">
    <div class="card-icon"><svg width="12" height="10" viewBox="0 0 12 10"><path d="M1 9V4l4-3h6v8z" fill="#fff"/></svg></div>
    <h3>Automotive</h3><p>All makes. All models.</p>
  </div>
  <div class="abs card-text" style="left:287px;top:780px">
    <div class="card-icon"><svg width="14" height="10" viewBox="0 0 14 10"><rect x="1" y="1" width="12" height="8" fill="none" stroke="#fff" stroke-width="1.4"/><path d="M4 1v8M7 1v8M10 1v8" stroke="#fff"/></svg></div>
    <h3>Commercial</h3><p>Store-fronts, Offices &amp; More.</p>
  </div>
  <div class="abs card-text" style="left:479px;top:780px">
    <div class="card-icon"><svg width="14" height="10" viewBox="0 0 14 10"><path d="M1 9V5l4-3 4 3v4zM9 9V4h4v5z" fill="#fff"/></svg></div>
    <h3>Residential</h3><p>Make Your Home Efficient.</p>
  </div>

  <div class="abs contact-bg"></div>
  <div class="abs contact-title">Contact Info</div>
  <div class="abs contact-underline"></div>
  <div class="abs contact-lead">Need to discuss ?</div>
  <div class="abs contact-row" style="top:1025px">
    <span class="circle-icon"><svg width="8" height="12" viewBox="0 0 8 12"><rect x="0.8" y="0.8" width="6.4" height="10.4" rx="1" fill="none" stroke="#fff" stroke-width="1.4"/></svg></span>
    <div><b>Phone:</b> 555.014.2290<br><b>Fax:</b> 555.014.2290</div>
  </div>
  <div class="abs contact-row" style="top:1065px">
    <span class="circle-icon"><svg width="10" height="13" viewBox="0 0 10 13"><path d="M5 12.5S1 7.5 1 5a4 4 0 0 1 8 0c0 2.5-4 7.5-4 7.5z" fill="#fff"/><circle cx="5" cy="5" r="1.5" fill="var(--teal)"/></svg></span>
    <div><b>4120 E. Palo Verde Rd. Suite B</b><br>Tempe Ridge, Az. 85000</div>
  </div>
  <div class="abs contact-row" style="top:1105px">
    <span class="circle-icon"><svg width="12" height="12" viewBox="0 0 12 12"><rect x="1" y="2" width="10" height="9" fill="none" stroke="#fff" stroke-width="1.2"/><path d="M1 4.5h10M4 2v9M8 2v9M1 7.5h10" stroke="#fff" stroke-width=".7"/></svg></span>
    <div><b style="font-size:7.5px">8:00am-5:00pm</b><br>Monday-Friday</div>
  </div>
  <div class="abs map" role="img" aria-label="Street map showing the shop location"></div>

  <div class="abs footer">Copyright © Mesa Tint, All Rights Reserved</div>
</div>
</body>
</html>
```